Halvorn - Refresh the look and feel of an existing website

We currently have an existing website www.halvornworldadvisory.example however it needs a more refreshed 'look and feel'. We are a professional consultancy that works with large corporate organisations and government. Our 'tag line' is A New Way of Thinking. We want the site to communicate "Innovation" and Leading Edge Thinking.

Target Market(s)

Corporate and Professional Clients - Organisation and Business Change

Industry/Entity Type

Management Consulting

Number of Pages Required

1 page

Font styles to use
Sans Serif

Requirements
Must have
• Must have a professional Corporate look and feel. Header 'imagery' is ok but boxes on front page need changing ... along with the words. The focus on home page needs to 'call out' 3 main consulting areas:-
• - Change & Transformation Specialists
• - Innovative Solutions
• - Digital Transformation
• Tag Line for business is ... A New Way of Thinking (Highlighting Halvorn as 'Thought Leaders' in business)
Nice to have
• Less "words' more imagery. Possibly an area for a 'video' or recent articles/blogs on the front page. Needs to have more of an 'interactive' feel. We are open to suggestions.
Should not have
• NA

```html
<!DOCTYPE html>
<html lang="en">
<head>
<meta charset="utf-8">
<title>Halvorn World Advisory</title>
<link rel="stylesheet" href="https://fonts.googleapis.com/css2?family=Questrial&family=Open+Sans:wght@400;600&display=swap">
<style>
:root{
  --navy:#253b56;
  --navy-deep:#1f3149;
  --gold:#f3a81b;
  --ink:#3f4a55;
  --heading:#4a4f55;
  --muted:#6d757c;
  --rule:#dcdfe2;
  --white:#ffffff;
  --foot-link:#a9b8c9;
  --foot-rule:#34506f;
}
*{box-sizing:border-box;margin:0;padding:0}
html,body{width:934px;height:1200px;overflow:hidden;background:var(--white)}
body{position:relative;font-family:"Open Sans",sans-serif;color:var(--ink)}
.abs{position:absolute}
h1,h2,h3,h4{font-weight:400}

/* hero */
.hero-photo{left:0;top:0;width:934px;height:463px;
  background:linear-gradient(90deg,#b9c6d3 0%,#8fa3b7 30%,#9aa8b3 50%,#6b5448 66%,#c9a58e 80%,#3a2c27 100%)}
.topbar{left:0;top:0;width:934px;height:53px;background:var(--navy);border-bottom:3px solid var(--gold)}
.nav{left:286px;top:0;height:50px;display:flex;font-family:"Questrial",sans-serif;font-size:14.5px}
.nav a{color:var(--white);text-decoration:none;padding:0 19px;line-height:50px}
.nav a.is-active{background:var(--gold);color:var(--navy);padding:0 14px}
.brand{left:20px;top:0;width:254px;height:95px}
.brand-name{left:44px;top:14px;display:flex;align-items:center;gap:12px;
  font-family:"Questrial",sans-serif;font-size:25px;color:var(--navy);letter-spacing:1px}
.brand-dot{width:54px;height:54px;border-radius:50%;background:var(--navy)}

.hero-panel{left:0;top:188px;width:448px;height:152px}
.hero-title{left:22px;top:201px;font-family:"Questrial",sans-serif;font-size:27px;color:var(--white)}
.hero-text{left:22px;top:245px;width:395px;font-family:"Questrial",sans-serif;font-size:15.5px;line-height:21px;color:var(--white)}
.hero-cta-frame{left:313px;top:300px}
.hero-cta{left:313px;top:300px;width:97px;height:28px;font-family:"Questrial",sans-serif;font-size:13.5px;color:var(--white);
  text-align:center;line-height:28px;text-decoration:none}

/* welcome */
.welcome-title{left:0;top:487px;width:934px;text-align:center;font-family:"Questrial",sans-serif;font-size:28px;color:var(--heading)}
.welcome-title strong{font-weight:400;color:var(--navy)}
.welcome-rule{left:22px;top:540px;width:890px;height:1px;background:var(--rule)}
.welcome-mark{left:453px;top:526px;width:28px;height:28px;border-radius:50%;background:var(--navy);border:4px solid var(--white);box-shadow:0 0 0 1px var(--rule)}
.intro{left:0;width:934px;text-align:center;font-family:"Questrial",sans-serif;font-size:14px;letter-spacing:0.25px;color:var(--muted)}

/* feature cards */
.card{width:243px;height:122px;border:2px solid var(--navy);background:var(--white)}
.card.is-featured{background:var(--navy)}
.card-title{position:absolute;left:50px;top:11px;white-space:nowrap;font-family:"Questrial",sans-serif;font-size:15.5px;color:var(--navy)}
.card-text{position:absolute;left:50px;top:37px;width:182px;height:52px;overflow:hidden;font-size:12.3px;line-height:17px;color:var(--muted)}
.card-more{position:absolute;left:51px;top:97px;font-size:10.5px;font-weight:600;color:var(--navy);text-decoration:none}
.is-featured .card-title,.is-featured .card-text,.is-featured .card-more{color:var(--white)}
.card-icon{width:78px;height:78px;border-radius:50%;background:var(--navy);display:flex;align-items:center;justify-content:center}
.card-icon.is-outlined{background:var(--white);border:2px solid var(--navy)}

/* footer */
.footer{left:0;top:954px;width:934px;height:204px;background:var(--navy);border-top:3px solid var(--gold)}
.foot-head{top:983px;font-family:"Questrial",sans-serif;font-size:15.5px;color:var(--gold)}
.foot-list{top:1018px;list-style:none;font-size:12px}
.foot-list li{height:25px;line-height:24px;color:var(--foot-link);border-bottom:1px solid var(--foot-rule)}
.foot-list li::before{content:"›";color:var(--white);margin-right:6px;font-size:14px}
.contact{left:704px;top:1016px;list-style:none;font-size:12px;color:var(--foot-link)}
.contact li{height:31px;display:flex;align-items:center;gap:8px;white-space:nowrap}
.contact .email{font-size:11px}
.bottom-bar{left:0;top:1158px;width:934px;height:42px;background:var(--white)}
.social{left:22px;top:1169px;display:flex;gap:14px}
.social span{width:20px;height:20px;border-radius:50%;background:var(--navy-deep)}
.copyright{right:22px;top:1170px;font-size:11.5px;color:var(--muted)}
</style>
</head>
<body>

<div class="abs hero-photo" role="img" aria-label="Photograph of a smiling professional woman looking upward in front of a blurred office building"></div>

<header>
  <div class="abs topbar"></div>
  <nav class="abs nav">
    <a class="is-active" href="#">Home</a>
    <a href="#">About</a>
    <a href="#">Our Services</a>
    <a href="#">Solutions</a>
    <a href="#">What's Happening</a>
    <a href="#">Contact Us</a>
  </nav>
  <svg class="abs brand" viewBox="0 0 254 95" aria-hidden="true">
    <polygon points="0,0 254,0 254,82 2,95" fill="#fff"/>
  </svg>
  <div class="abs brand-name"><span class="brand-dot"></span>HALVORN</div>
</header>

<section class="hero">
  <svg class="abs hero-panel" viewBox="0 0 448 152" aria-hidden="true">
    <polygon points="0,0 378,0 448,152 0,152" fill="#2e4662" fill-opacity="0.72"/>
  </svg>
  <h1 class="abs hero-title">A New Way of Thinking.</h1>
  <p class="abs hero-text">Thought leaders for business - specialists delivering the outcomes our clients want.</p>
  <svg class="abs hero-cta-frame" width="97" height="28" aria-hidden="true">
    <path d="M1 10 V1 H18 M96 18 V27 H79" fill="none" stroke="#fff" stroke-width="2"/>
  </svg>
  <a class="abs hero-cta" href="#">Learn more</a>
</section>

<section class="welcome">
  <h2 class="abs welcome-title">Welcome to <strong>Halvorn</strong></h2>
  <div class="abs welcome-rule"></div>
  <div class="abs welcome-mark"></div>
  <p class="abs intro" style="top:570px">The team at Halvorn World Advisory has wide ranging experience and is well-placed to support all aspects of our global community.</p>
  <p class="abs intro" style="top:598px">All of our models and programs are leading edge - A New Way of Thinking for the 21st Century.</p>
</section>

<section class="features">
  <article class="abs card is-featured" style="left:60px;top:646px">
    <h3 class="card-title">Change &amp; Transformation</h3>
    <p class="card-text">Specialists guiding large organisations through change with confidence.</p>
    <a class="card-more" href="#">Read More</a>
  </article>
  <div class="abs card-icon is-outlined" style="left:21px;top:668px">
    <svg width="38" height="38" viewBox="0 0 38 38" aria-hidden="true"><path d="M31 14A13 13 0 0 0 7 13" fill="none" stroke="#253b56" stroke-width="3"/><path d="M7 24a13 13 0 0 0 24 1" fill="none" stroke="#253b56" stroke-width="3"/><path d="M3 7v8h8M35 31v-8h-8" fill="none" stroke="#253b56" stroke-width="3"/></svg>
  </div>

  <article class="abs card" style="left:364px;top:646px">
    <h3 class="card-title">Innovative Solutions</h3>
    <p class="card-text">A new way of thinking that delivers leading edge, sustainable solutions.</p>
    <a class="card-more" href="#">Read More</a>
  </article>
  <div class="abs card-icon" style="left:326px;top:668px">
    <svg width="30" height="38" viewBox="0 0 30 38" aria-hidden="true"><path d="M15 2a12 12 0 0 0-7 22v5h14v-5A12 12 0 0 0 15 2z" fill="none" stroke="#fff" stroke-width="2.5"/><path d="M9 33h12M11 37h8" stroke="#fff" stroke-width="2.5"/></svg>
  </div>

  <article class="abs card" style="left:668px;top:646px">
    <h3 class="card-title">Digital Transformation</h3>
    <p class="card-text">Helping corporate and government clients embrace digital ways of working.</p>
    <a class="card-more" href="#">Read More</a>
  </article>
  <div class="abs card-icon" style="left:630px;top:668px">
    <svg width="40" height="34" viewBox="0 0 40 34" aria-hidden="true"><rect x="2" y="2" width="36" height="23" rx="2" fill="none" stroke="#fff" stroke-width="2.5"/><path d="M14 32h12M20 25v7" stroke="#fff" stroke-width="2.5"/><path d="M15 10l-4 3.5 4 3.5M25 10l4 3.5-4 3.5" fill="none" stroke="#fff" stroke-width="2.5"/></svg>
  </div>

  <article class="abs card" style="left:60px;top:792px">
    <h3 class="card-title">Development Programs</h3>
    <p class="card-text">We support all elements of organisational development with leading programs.</p>
    <a class="card-more" href="#">Read More</a>
  </article>
  <div class="abs card-icon" style="left:21px;top:814px">
    <svg width="40" height="32" viewBox="0 0 40 32" aria-hidden="true"><rect x="2" y="2" width="36" height="28" rx="2" fill="none" stroke="#fff" stroke-width="2.5"/><path d="M2 9h36M15 15l-5 5 5 5M25 15l5 5-5 5" fill="none" stroke="#fff" stroke-width="2.5"/></svg>
  </div>

  <article class="abs card" style="left:364px;top:792px">
    <h3 class="card-title">Giving Back</h3>
    <p class="card-text">A core value for Halvorn is supporting our broader Community and Environment</p>
    <a class="card-more" href="#">Read More</a>
  </article>
  <div class="abs card-icon" style="left:326px;top:814px">
    <svg width="34" height="32" viewBox="0 0 34 32" aria-hidden="true"><path d="M17 29S3 20 3 11a7 7 0 0 1 14-2 7 7 0 0 1 14 2c0 9-14 18-14 18z" fill="none" stroke="#fff" stroke-width="2.5"/></svg>
  </div>

  <article class="abs card" style="left:668px;top:792px">
    <h3 class="card-title">What's Happening</h3>
    <p class="card-text">Browse our latest articles, blogs and thought leadership on new thinking.</p>
    <a class="card-more" href="#">Read More</a>
  </article>
  <div class="abs card-icon" style="left:630px;top:814px">
    <svg width="38" height="32" viewBox="0 0 38 32" aria-hidden="true"><rect x="2" y="2" width="34" height="20" rx="10" fill="none" stroke="#fff" stroke-width="2.5"/><path d="M10 22l-4 8 10-8" fill="#fff"/><circle cx="12" cy="12" r="2" fill="#fff"/><circle cx="19" cy="12" r="2" fill="#fff"/><circle cx="26" cy="12" r="2" fill="#fff"/></svg>
  </div>
</section>

<footer>
  <div class="abs footer"></div>
  <h4 class="abs foot-head" style="left:22px">About Us</h4>
  <ul class="abs foot-list" style="left:22px;width:78px">
    <li>Our Team</li><li>Our Clients</li><li>Our Values</li><li>Giving Back</li>
  </ul>
  <h4 class="abs foot-head" style="left:229px">Our Services</h4>
  <ul class="abs foot-list" style="left:229px;width:175px">
    <li>Strategy and Design</li><li>Transformation</li><li>Change &amp; Culture</li><li>Organisational Development</li>
  </ul>
  <ul class="abs foot-list" style="left:447px;width:154px">
    <li>Project Management</li><li>Organisational Efficiency</li><li>Specialist Placements</li>
  </ul>
  <h4 class="abs foot-head" style="left:704px">Contact Us</h4>
  <ul class="abs contact">
    <li><svg width="14" height="14" viewBox="0 0 14 14" aria-hidden="true"><path d="M3 1l3 3-2 2c1 2 2 3 4 4l2-2 3 3-2 2C6 13 1 8 1 3z" fill="#fff"/></svg>(Aus) 1300 - 000 - 512</li>
    <li><svg width="14" height="14" viewBox="0 0 14 14" aria-hidden="true"><path d="M3 1l3 3-2 2c1 2 2 3 4 4l2-2 3 3-2 2C6 13 1 8 1 3z" fill="#fff"/></svg>(NZ) 0800 - 080 - 512</li>
    <li><svg width="14" height="14" viewBox="0 0 14 14" aria-hidden="true"><path d="M3 1l3 3-2 2c1 2 2 3 4 4l2-2 3 3-2 2C6 13 1 8 1 3z" fill="#fff"/></svg>(Intl) 1300 - 000 - 513</li>
    <li class="email"><svg width="14" height="12" viewBox="0 0 14 12" aria-hidden="true"><rect x="1" y="1" width="12" height="10" fill="none" stroke="#fff" stroke-width="1.5"/><path d="M1 1l6 5 6-5" fill="none" stroke="#fff" stroke-width="1.5"/></svg>info@halvornworldadvisory.example</li>
  </ul>
  <div class="abs bottom-bar"></div>
  <div class="abs social"><span></span><span></span><span></span><span></span></div>
  <p class="abs copyright">Copyright © 2014 Halvorn World Advisory</p>
</footer>

</body>
</html>
```